Business card for exciting VC company

Should look simple, crisp, and modern.

Industry/Entity Type

Venture Capital

Contact Information for Business Card

Would like to see at least one design that has our blue on the back with the tagline "Modernizing Essential Businesses" and white front with contact details.

Font styles to use
Sans Serif

Requirements
Must have
• Logo

Gregory Tallis
gtallis@brindlewave.vc
Managing Partner
M (628)354-xxxx

```html
<!DOCTYPE html>
<html lang="en">
<head>
<meta charset="utf-8">
<title>Brindlewave Capital – Business Card</title>
<link href="https://fonts.googleapis.com/css2?family=Lato:wght@400;700&display=swap" rel="stylesheet">
<style>
  :root {
    --brand-blue: #4281c4;
    --ink: #111111;
    --text-grey: #5c5c5c;
    --paper: #ffffff;
    --backdrop: #ddd6cc;
  }
  * { box-sizing: border-box; margin: 0; padding: 0; }
  html, body { width: 1200px; height: 965px; overflow: hidden; }
  body { background: var(--backdrop); position: relative; font-family: "Lato", sans-serif; }

  .card {
    position: absolute;
    left: 278px;
    width: 647px;
    height: 369px;
    border-radius: 24px;
    overflow: hidden;
  }
  .card--back { top: 98px; background: var(--brand-blue); }
  .card--front { top: 504px; background: var(--paper); }

  .wordmark {
    position: absolute;
    font-family: "Lato", sans-serif;
    font-weight: 700;
    color: var(--ink);
    text-align: center;
    line-height: 1;
  }
  .wordmark__name, .wordmark__sub { display: block; }

  .card--back .wordmark { left: 0; right: 0; top: 114px; }
  .card--back .wordmark__name { font-size: 60px; letter-spacing: 2px; }
  .card--back .wordmark__sub { font-size: 24px; letter-spacing: 10px; margin-top: 14px; padding-left: 10px; }

  .tagline {
    position: absolute;
    left: 0; right: 0; top: 228px;
    text-align: center;
    font-weight: 700;
    font-size: 19px;
    color: var(--paper);
  }

  .card--front .wordmark { left: 30px; width: 282px; top: 152px; }
  .card--front .wordmark__name { font-size: 37px; letter-spacing: 1px; }
  .card--front .wordmark__sub { font-size: 16px; letter-spacing: 6px; margin-top: 8px; padding-left: 6px; }

  .divider {
    position: absolute;
    left: 319px; top: 94px;
    width: 2px; height: 178px;
    background: var(--brand-blue);
  }

  .person { position: absolute; left: 337px; top: 112px; }
  .person__name { font-weight: 700; font-size: 26px; color: var(--ink); text-transform: uppercase; line-height: 1.15; }
  .person__role { font-size: 18px; color: var(--text-grey); margin-top: 1px; }

  .contacts { position: absolute; left: 338px; top: 182px; list-style: none; }
  .contacts li {
    display: flex; align-items: center;
    height: 24px;
    font-size: 18px;
    color: var(--text-grey);
  }
  .contacts svg { width: 16px; height: 16px; margin-right: 10px; flex: none; }

  .footer-band {
    position: absolute; left: 0; right: 0; bottom: 0;
    height: 12px; background: var(--brand-blue);
  }
</style>
</head>
<body>

<section class="card card--back" aria-label="Card back">
  <div class="wordmark">
    <span class="wordmark__name">BRINDLEWAVE</span>
    <span class="wordmark__sub">CAPITAL</span>
  </div>
  <p class="tagline">MODERNIZING ESSENTIAL BUSINESSES</p>
</section>

<section class="card card--front" aria-label="Card front">
  <div class="wordmark">
    <span class="wordmark__name">BRINDLEWAVE</span>
    <span class="wordmark__sub">CAPITAL</span>
  </div>
  <div class="divider"></div>
  <div class="person">
    <h1 class="person__name">Gregory Tallis</h1>
    <p class="person__role">Managing Partner</p>
  </div>
  <ul class="contacts">
    <li>
      <svg viewBox="0 0 24 24" aria-hidden="true"><path fill="#4281c4" d="M6.6 10.8a15 15 0 0 0 6.6 6.6l2.2-2.2c.3-.3.7-.4 1-.2 1.1.4 2.3.6 3.6.6.6 0 1 .4 1 1V20c0 .6-.4 1-1 1C10.6 21 3 13.4 3 4c0-.6.4-1 1-1h3.5c.6 0 1 .4 1 1 0 1.3.2 2.5.6 3.6.1.3 0 .7-.2 1z"/></svg>
      (628)354-xxxx
    </li>
    <li>
      <svg viewBox="0 0 24 24" aria-hidden="true"><rect x="2" y="5" width="20" height="14" rx="1" fill="#4281c4"/><path d="M2.5 6l9.5 7 9.5-7" fill="none" stroke="#fff" stroke-width="1.6"/></svg>
      gtallis@brindlewave.vc
    </li>
    <li>
      <svg viewBox="0 0 24 24" aria-hidden="true"><circle cx="12" cy="12" r="10" fill="#4281c4"/><path d="M2 12h20M12 2c3 3 3 17 0 20M12 2c-3 3-3 17 0 20" fill="none" stroke="#fff" stroke-width="1.3"/></svg>
      www.brindlewave.vc
    </li>
  </ul>
  <div class="footer-band"></div>
</section>

</body>
</html>
```